Computer Company needs a Business card design

We need a business card design for our business. We assist people to transition to the QLX (Quorra Linkwave Exchange). The Australian Government-owned qlx™ network is a brand new telecommunications network currently being rolled out across Australia, giving access to a reliable broadband connection. Our niche market will predominantly be domestic customers in the 50+ age bracket. The assistance that we provide is everything from arranging the equipment, arranging the plan and contract term, appointment times, final testing of the network and any tweaks that need to be made. We basically PM the transition from start to finish. The business card design should be minimalist, should communicate loyalty and stability, should be easy to read and clearly explain what we do. We have asked for front and back. However, the back of the card does not have to include much information at all. It could be just a small design, or a repeat of our phone number. Up to you. The attached file only says what is required on the card. It does not specify where to arrange the text, what fonts to use, etc etc. As much as we would like to give you more info, due to our very limited design ability, we are not really able to send you any rough, or otherwise, designs of what we are after. Hopefully the above description is enough for you.

```html
<!DOCTYPE html>
<html lang="en">
<head>
<meta charset="utf-8">
<title>QLXME Business Card</title>
<link rel="stylesheet" href="https://fonts.googleapis.com/css2?family=Bebas+Neue&display=swap">
<style>
  :root {
    --card-bg-light: #1f2122;
    --card-bg-dark: #131415;
    --brand-blue: #2450f5;
    --ink-white: #ffffff;
  }
  * { margin: 0; padding: 0; box-sizing: border-box; }
  html, body {
    width: 1200px;
    height: 686px;
    overflow: hidden;
    background: var(--card-bg-dark);
  }
  .business-card {
    position: relative;
    width: 1200px;
    height: 686px;
    overflow: hidden;
    font-family: "Bebas Neue", "Arial Narrow", sans-serif;
    color: var(--ink-white);
  }
  .card-texture {
    position: absolute;
    inset: 0;
    background: radial-gradient(ellipse at 50% 45%, var(--card-bg-light) 0%, var(--card-bg-dark) 100%);
  }
  .brand-square {
    position: absolute;
    left: 564px;
    top: 140px;
    width: 72px;
    height: 72px;
    background: var(--brand-blue);
  }
  .brand-name {
    position: absolute;
    left: 0;
    width: 100%;
    top: 232px;
    text-align: center;
    font-size: 196px;
    line-height: 1;
    letter-spacing: -1px;
    color: var(--ink-white);
  }
  .brand-tagline {
    position: absolute;
    left: 0;
    width: 100%;
    top: 402px;
    text-align: center;
    font-size: 32px;
    line-height: 1;
    letter-spacing: 2px;
    text-transform: uppercase;
  }
  .web-address {
    position: absolute;
    left: 0;
    width: 100%;
    top: 548px;
    text-align: center;
    font-size: 36px;
    line-height: 1;
    letter-spacing: 12.5px;
    text-transform: uppercase;
    padding-left: 12px;
  }
</style>
</head>
<body>
  <main class="business-card">
    <div class="card-texture" role="img" aria-label="Dark charcoal pixel-block texture background"></div>
    <div class="brand-square" aria-hidden="true"></div>
    <h1 class="brand-name">QLXME</h1>
    <p class="brand-tagline">Quorra Linkwave Exchange</p>
    <p class="web-address">www.qlxmadeeasy.com.au</p>
  </main>
</body>
</html>
```